Vantrel - corporate Business Card

We need a good look and innovative business card for a new start up company based in Los Angeles called "Vantrel". We are in a payment business, including payment card, app, and ewallet. We are expert in online payment and Card not present (CNP) transaction.
We need an innovative, modern business card.

Our logo font is Aero Matics

Target Market(s)

Startup - Bank - Online Payment - Card Manufacturing

Industry/Entity Type

Startup

Contact Information for Business Card

phone: 555 371 6042 - Address: 4270 Marrowgate blvd, Harlow Bay, CA 90417

Requirements
Must have
• Message: innovative, professional, expert, high tech, trust, online payment expert, security
Nice to have
• no comment
Should not have
• no Comment

```html
<!DOCTYPE html>
<html lang="en">
<head>
<meta charset="utf-8">
<title>Vantrel – Business Card</title>
<link href="https://fonts.googleapis.com/css2?family=Lato:wght@400;700&display=swap" rel="stylesheet">
<style>
  :root {
    --brand-red: #b81f2f;
    --brand-red-faint: #f0dadd;
    --card-bg: #f5f5f5;
    --page-bg: #ececec;
    --ink: #1c1c1c;
    --white: #ffffff;
  }
  * { margin: 0; padding: 0; box-sizing: border-box; }
  html, body { width: 1200px; height: 586px; overflow: hidden; }
  body {
    background: var(--page-bg);
    font-family: "Lato", sans-serif;
    position: relative;
  }
  .card {
    position: absolute;
    top: 129px;
    width: 502px;
    height: 301px;
    background: var(--card-bg);
    overflow: hidden;
  }
  .card--front { left: 61px; }
  .card--back { left: 619px; }

  /* Front */
  .front-circle {
    position: absolute;
    left: 120px; top: 19px;
    width: 262px; height: 262px;
    border-radius: 50%;
    background: var(--brand-red-faint);
  }
  .front-name {
    position: absolute;
    left: 0; right: 0; top: 124px;
    text-align: center;
    font-weight: 700;
    font-size: 40px;
    line-height: 48px;
    color: var(--brand-red);
    letter-spacing: 1px;
  }
  .front-web {
    position: absolute;
    left: 0; right: 0; top: 265px;
    text-align: center;
    font-weight: 700;
    font-size: 11px;
    line-height: 14px;
    letter-spacing: 3.4px;
    color: var(--brand-red);
  }

  /* Back */
  .brand {
    position: absolute;
    top: 33px; left: 0; right: 0;
    display: flex; align-items: center; justify-content: center;
    gap: 10px;
  }
  .brand-dot {
    width: 64px; height: 64px;
    border-radius: 50%;
    background: var(--brand-red);
  }
  .brand-name {
    font-weight: 700;
    font-size: 40px;
    line-height: 48px;
    color: var(--brand-red);
    letter-spacing: 1px;
  }
  .person {
    position: absolute;
    right: 295px; top: 167px;
    text-align: right;
  }
  .person-name {
    font-weight: 700;
    font-size: 16px;
    line-height: 20px;
    color: var(--brand-red);
  }
  .person-role {
    margin-top: 3px;
    font-size: 10.5px;
    line-height: 14px;
    color: var(--ink);
  }
  .divider {
    position: absolute;
    left: 235px; top: 139px;
    width: 2px; height: 108px;
    background: linear-gradient(to bottom, transparent, var(--brand-red) 30%, var(--brand-red) 70%, transparent);
  }
  .contact {
    position: absolute;
    left: 262px; top: 168px;
    list-style: none;
  }
  .contact-item {
    display: flex; align-items: center; gap: 7px;
    font-size: 12px;
    line-height: 18px;
    color: var(--ink);
    height: 18px;
    margin-bottom: 7px;
    white-space: nowrap;
  }
  .contact-icon { width: 18px; height: 18px; flex: none; }
  .address-band {
    position: absolute;
    left: 0; right: 0; bottom: 0;
    height: 30px;
    background: var(--brand-red);
    color: var(--white);
    font-weight: 700;
    font-size: 12px;
    display: flex; align-items: center; justify-content: center;
    white-space: nowrap;
  }
</style>
</head>
<body>
  <section class="card card--front" aria-label="Business card front">
    <div class="front-circle"></div>
    <div class="front-name">Vantrel</div>
    <div class="front-web">www.vantrelwebsite.com</div>
  </section>

  <section class="card card--back" aria-label="Business card back">
    <div class="brand">
      <div class="brand-dot"></div>
      <div class="brand-name">Vantrel</div>
    </div>

    <div class="person">
      <div class="person-name">Marcus Hale</div>
      <div class="person-role">Owner &amp; Founder</div>
    </div>

    <div class="divider"></div>

    <ul class="contact">
      <li class="contact-item">
        <svg class="contact-icon" viewBox="0 0 18 18" aria-hidden="true">
          <circle cx="9" cy="9" r="9" fill="var(--brand-red)"/>
          <path d="M5 7.5c0-1.2 1.8-2 4-2s4 .8 4 2v.6h-2v-.8H7v.8H5z" fill="#fff"/>
          <rect x="5.5" y="9" width="7" height="3.5" rx="0.8" fill="#fff"/>
        </svg>
        <span>(555) 371-6042</span>
      </li>
      <li class="contact-item">
        <svg class="contact-icon" viewBox="0 0 18 18" aria-hidden="true">
          <circle cx="9" cy="9" r="9" fill="var(--brand-red)"/>
          <rect x="4.5" y="6" width="9" height="6.5" fill="#fff"/>
          <path d="M4.5 6l4.5 3.6L13.5 6" fill="none" stroke="var(--brand-red)" stroke-width="0.9"/>
        </svg>
        <span>MarcusH@vantrelweb.com</span>
      </li>
    </ul>

    <div class="address-band">4270 Marrowgate blvd, Harlow Bay, CA 90417</div>
  </section>
</body>
</html>
```